Business Card and Stationary Design

After the successful redesign of our logo we are wanting to follow suite and create a new business card and stationary design!

New Logo is attached, information required on the business card should contain a mixture of the following but layout/arrangement is up to the designer.

Happy if the national provider number and abn are on the back, and happy for them to be smaller than the rest.

I am also happy to receive single sided or weird and wonderful designs.

Name
Title
National Provider Number 7291
ABN 53 219 864 317
Level 3, 42 Marlow Street
Hollins Bay NSW 2291
Ph: 1300 987 214
Mobile: 0432 785 619
name@ferngatebuild.com.au
www.ferngatebuild.com.au

Target Market(s)

Professionals, Peers, Students, Suppliers...

Industry/Entity Type

Construction

Contact Information for Business Card

Listed in project description

Font styles to use
Other font styles liked:
• Century Gothic

Colors
0455a3
3176b5
ffffff

Requirements
Must have
• Professional Design, same color scheme as our logo
Nice to have
• Something that sets our apart from everyone else would be fantastic, open to size and shape and layout options, as long as they present professionally.
• Open to raised/embossed text, alternative materials, custom sizes, clear material
Should not have
• The color orange

```html
<!DOCTYPE html>
<html lang="en">
<head>
<meta charset="utf-8">
<title>Ferngate Build – Business Card</title>
<link rel="stylesheet" href="https://fonts.googleapis.com/css2?family=Open+Sans:wght@400;600;700&display=swap">
<style>
  :root {
    --page: #e9e9ea;
    --card: #161719;
    --brand-blue: #3176b5;
    --brand-deep: #0455a3;
    --text: #ffffff;
    --muted: #9a9ca0;
    --rule: #d8d9dc;
  }
  * { box-sizing: border-box; margin: 0; padding: 0; }
  html, body {
    width: 1200px; height: 864px; overflow: hidden;
    background: var(--page);
    font-family: "Open Sans", sans-serif;
  }
  .sheet {
    width: 1200px; height: 864px;
    display: flex; align-items: center; justify-content: center; gap: 48px;
  }
  .card {
    width: 540px; height: 310px;
    background: var(--card);
    border-radius: 4px;
    box-shadow: 0 10px 24px rgba(0,0,0,.25);
    position: relative;
    overflow: hidden;
  }
  /* Front */
  .card-front {
    display: flex; flex-direction: column; align-items: center; justify-content: center;
  }
  .front-brand {
    display: flex; align-items: center; gap: 14px;
    color: #5a5c60; font-weight: 700; font-size: 40px; letter-spacing: .5px;
  }
  .front-brand .brand-square { width: 26px; height: 26px; background: #3a3c40; }
  .front-url {
    margin-top: 34px;
    color: var(--muted); font-size: 13px; letter-spacing: 6px;
  }
  /* Details side */
  .card-details { display: flex; }
  .brand-block {
    width: 270px; padding-left: 26px;
    display: flex; flex-direction: column; justify-content: center;
  }
  .brand-name {
    display: flex; align-items: center; gap: 10px;
    color: var(--brand-blue); font-weight: 600; font-size: 28px; line-height: 1;
  }
  .brand-name .brand-square { width: 20px; height: 20px; background: var(--brand-deep); }
  .brand-legal {
    margin: 6px 0 0 30px;
    color: var(--brand-blue); font-size: 11px; font-weight: 600; letter-spacing: 1.5px; text-transform: uppercase;
  }
  .brand-tagline {
    margin: 3px 0 0 30px;
    color: var(--muted); font-size: 7.5px; letter-spacing: 1px; text-transform: uppercase;
  }
  .divider {
    width: 2px; margin: 40px 0;
    background: linear-gradient(to bottom, transparent, var(--rule) 30%, var(--rule) 70%, transparent);
  }
  .contact-block {
    flex: 1; padding: 34px 16px 0 22px;
    color: var(--text); font-size: 13.5px; line-height: 1.34;
    white-space: nowrap;
  }
  .person-name { color: var(--brand-blue); font-weight: 700; font-size: 14.5px; letter-spacing: .5px; }
  .person-title { margin-bottom: 10px; }
  .address { margin-bottom: 4px; }
  .contact-line { display: flex; align-items: center; gap: 8px; }
  .contact-line svg { width: 12px; height: 12px; fill: var(--text); flex: none; }
  .legal { margin-top: 2px; }
</style>
</head>
<body>
<main class="sheet">
  <section class="card card-front">
    <div class="front-brand"><span class="brand-square"></span>ferngatebuild</div>
    <p class="front-url">www.ferngatebuild.com.au</p>
  </section>

  <section class="card card-details">
    <div class="brand-block">
      <div class="brand-name"><span class="brand-square"></span>ferngate build</div>
      <p class="brand-legal">Ferngate Build Pty Ltd</p>
      <p class="brand-tagline">Design • Build • Renovate • Maintain</p>
    </div>
    <div class="divider"></div>
    <div class="contact-block">
      <p class="person-name">DANIEL HART</p>
      <p class="person-title">CEO/FOUNDER</p>
      <p>Level 3, 42 Marlow Street</p>
      <p class="address">Hollins Bay NSW 2291</p>
      <p class="contact-line">
        <svg viewBox="0 0 12 12" aria-hidden="true"><path d="M2 1h2.5l1 3-1.5 1a6 6 0 0 0 3 3l1-1.5 3 1V10a1 1 0 0 1-1 1A9 9 0 0 1 1 2a1 1 0 0 1 1-1z"/></svg>1300 987 214</p>
      <p class="contact-line">
        <svg viewBox="0 0 12 12" aria-hidden="true"><path d="M3 0h6a1 1 0 0 1 1 1v10a1 1 0 0 1-1 1H3a1 1 0 0 1-1-1V1a1 1 0 0 1 1-1zm0 1.5v8h6v-8z"/></svg>0432 785 619</p>
      <p class="contact-line">
        <svg viewBox="0 0 12 12" aria-hidden="true"><path d="M0 2h12v1L6 7 0 3zm0 2.2 6 4 6-4V10H0z"/></svg>name@ferngatebuild.com.au</p>
      <p class="contact-line">
        <svg viewBox="0 0 12 12" aria-hidden="true"><circle cx="6" cy="6" r="6"/><path d="M6 1v10M1 6h10" stroke="#161719" stroke-width="1"/></svg>www.ferngatebuild.com.au</p>
      <p class="legal">National Provider Number 7291</p>
      <p>ABN 53 219 864 317</p>
    </div>
  </section>
</main>
</body>
</html>
```